Existing WP site needs a fresh look (design only)

The current website, www.tarnbelle.com.au, is fine, but needs a fresh look so their clients can tell their website has been 'refreshed' regularly.
https://www.tarnbelle.com.au/sitemap/
They will use the existing functionality.
They want to keep the blue, green and white of their logo as the main colors, but a fresh look. They prefer a light look to a dark look, but they would be open to good designs that change their mind.
Be creative, think outside the box.
You only need to supply the 'home page ' design to win but the winners will be asked to provide an extra 'standard' page template (like the one currently being used for search results and other pages)
Any photos used must be supplied without charge with the PSDs in a resolution acceptable for the WordPress site.
2 page

```html
<!DOCTYPE html>
<html lang="en">
<head>
<meta charset="utf-8">
<title>Tarnbelle Voices – Home</title>
<link href="https://fonts.googleapis.com/css2?family=Oswald:wght@500;600&family=Roboto:wght@400;500;700&display=swap" rel="stylesheet">
<style>
:root{
  --navy:#1b3a5a;
  --green:#6aa82a;
  --text:#555b62;
  --white:#fff;
}
*{box-sizing:border-box;margin:0;padding:0}
html,body{width:1200px;height:3401px;overflow:hidden;background:var(--white)}
body{position:relative;font-family:"Roboto",Arial,sans-serif;color:var(--text)}
.abs{position:absolute}
.h-title{font-family:"Oswald",Impact,sans-serif;font-weight:600;text-transform:uppercase;letter-spacing:.2px;color:var(--navy)}
.h-title .accent{color:var(--green)}
.btn{position:absolute;display:flex;align-items:center;justify-content:center;gap:10px;background:var(--green);color:#fff;font-weight:700;font-size:15px;text-transform:uppercase}
.social{display:flex;gap:12px}
.social span{width:30px;height:30px;border-radius:50%;background:#fff;box-shadow:0 2px 5px rgba(0,0,0,.2);display:block;position:relative}
.social span::after{content:"";position:absolute;left:11px;top:11px;width:8px;height:8px;border-radius:50%;background:var(--green)}

/* header */
.site-header{top:0;left:0;width:1200px;height:92px;border-top:4px solid var(--green);background:#fff}
.brand{position:absolute;display:flex;align-items:center;gap:8px;font-family:"Oswald",sans-serif;font-weight:600;color:var(--navy)}
.brand .mark{width:14px;height:14px;background:var(--green);border-radius:2px}
.brand .stack{display:flex;flex-direction:column;line-height:1}
.brand .stack small{font-family:"Roboto",sans-serif;font-weight:400;font-size:.6em;letter-spacing:1px;margin-top:3px}
.site-header .brand{left:110px;top:20px;font-size:24px}
.main-nav{left:334px;top:36px;display:flex;gap:25px;font-weight:500;font-size:15.5px;color:var(--navy)}
.main-nav .current{color:var(--green)}
.site-header .social{position:absolute;left:928px;top:31px}

/* hero */
.hero{top:92px;left:0;width:1200px;height:600px;background:radial-gradient(ellipse at 75% 30%,#8b6fd8 0%,#3a2f8a 35%,#1b1d4a 70%),#222}
.hero-photo{position:absolute;inset:0;background:linear-gradient(160deg,rgba(210,80,120,.35) 0%,rgba(40,30,110,.2) 45%,rgba(200,190,230,.45) 80%)}
.hero-card{position:absolute;left:282px;top:185px;width:636px;height:228px;background:rgba(232,234,240,.9);text-align:center}
.hero-card h1{font-size:29px;margin-top:22px}
.hero-card p{font-size:17.5px;font-weight:500;color:var(--navy);line-height:28px;margin-top:12px}
.hero-card .btn{left:243px;top:147px;width:150px;height:52px}

/* about */
.about-frame{left:111px;top:787px;width:430px;height:343px;border:6px solid var(--green);border-right:none}
.about-frame::after{content:"";position:absolute;right:-1px;top:-6px;width:6px;height:20px;background:var(--green)}
.about-photo{left:127px;top:802px;width:430px;height:344px;background:#fff;box-shadow:0 0 8px rgba(0,0,0,.15);padding:8px 7px}
.about-photo div{width:100%;height:100%;background:linear-gradient(135deg,#5d6266,#2c2f33 60%,#494d52)}
.about h2{left:607px;top:826px;font-size:37px}
.about p{left:607px;top:900px;width:473px;font-size:13.8px;line-height:25px;text-align:justify;color:#666}
.about .btn{left:607px;top:1058px;width:141px;height:51px;font-size:14.5px}

/* spotlight */
.spotlight{top:1243px;left:0;width:1200px;height:471px;background:linear-gradient(100deg,#203f5e 0%,#28496a 45%,#1c3b5b 100%)}
.spotlight h2{position:absolute;left:111px;top:104px;font-size:36px;color:#fff}
.spotlight .quote{position:absolute;left:112px;top:177px;width:490px;font-size:14px;line-height:25px;color:#fff}
.spotlight .artist{position:absolute;left:112px;top:247px;color:#fff;font-weight:700;font-size:19px}
.spotlight .artist small{font-weight:400;font-size:14.5px}
.spotlight .btn{left:111px;top:307px;width:143px;height:51px}
.play{width:13px;height:13px;border-radius:50%;background:#fff;position:relative}
.play::after{content:"";position:absolute;left:5px;top:3.5px;border-left:5px solid var(--green);border-top:3px solid transparent;border-bottom:3px solid transparent}
.sl-arrow{position:absolute;top:314px;width:38px;height:38px;display:flex;align-items:center;justify-content:center}
.sl-arrow.prev{left:514px;background:#8a9aa8}
.sl-arrow.next{left:561px;background:#fff}
.spot-photo{position:absolute;left:660px;top:65px;width:429px;height:342px;background:linear-gradient(135deg,#6a5b4d,#3a3330 55%,#1f1f22)}

/* testimonials */
.testimonials h2{left:0;width:1200px;top:1800px;text-align:center;font-size:37px}
.t-card{top:1888px;width:480px;height:211px;background:#fff;box-shadow:0 0 9px rgba(0,0,0,.16);padding:24px 34px 0 36px}
.t-card p{font-size:15px;line-height:26px;color:#666}
.t-card .who{display:flex;align-items:center;gap:22px;margin-top:16px}
.t-card .avatar{width:64px;height:64px;border-radius:50%;background:#e6e6e6;flex:none}
.t-card .org{font-weight:700;font-size:19.5px;color:var(--green)}
.t-card .role{font-weight:500;font-size:14px;color:var(--navy);margin-top:5px}
.side-arrow{top:1975px}

/* clients */
.clients{top:2196px;left:0;width:1200px;height:229px;background:linear-gradient(90deg,#23456a,#2b4d70 50%,#23456a)}
.clients h2{position:absolute;left:0;width:1200px;top:52px;text-align:center;font-size:37px;color:#fff}
.client-row{position:absolute;left:111px;top:128px;width:978px;display:flex;justify-content:space-between;align-items:center;font-weight:700;font-size:25px;color:#c9d1d9}
.clients .side-arrow{top:138px}

/* news */
.news h2{left:0;width:1200px;top:2512px;text-align:center;font-size:37px}
.n-card{top:2590px;width:313px;height:335px;background:#fff;box-shadow:0 0 9px rgba(0,0,0,.16);padding:8px}
.n-card .thumb{height:206px}
.n-card h3{font-weight:500;font-size:20.5px;line-height:25px;color:var(--navy);text-transform:uppercase;margin:12px 0 0 -1px}
.n-card .date{display:inline-block;margin-top:12px;background:var(--green);color:#fff;font-size:12px;padding:6px 16px}

/* footer */
.site-footer{top:3020px;left:0;width:1200px;height:332px;background:var(--navy)}
.site-footer .brand{left:0;width:1200px;justify-content:center;top:42px;font-size:40px;color:#fff}
.site-footer .brand .mark{width:22px;height:22px}
.foot-nav{position:absolute;left:0;width:1200px;top:152px;display:flex;justify-content:center;gap:31px;color:#fff;font-weight:500;font-size:20px}
.foot-line{position:absolute;left:0;width:1200px;text-align:center;color:#fff;font-weight:500;font-size:14.5px;display:flex;justify-content:center;align-items:center;gap:8px}
.site-footer .social{position:absolute;left:518px;top:275px;gap:9px}
.site-footer .social span{width:34px;height:34px;box-shadow:none}
.site-footer .social span::after{left:13px;top:13px}
.copyright{top:3352px;left:0;width:1200px;height:49px;background:var(--green);color:#fff;font-size:12.5px;text-align:center;line-height:49px}
</style>
</head>
<body>

<header class="site-header abs">
  <div class="brand"><span class="stack">TARNBELLE<small>VOICES</small></span><span class="mark"></span></div>
  <nav class="main-nav abs">
    <span class="current">Home</span><span>About Us</span><span>Shortlist</span><span>Voices</span><span>Rates</span><span>News</span><span>Contact Us</span>
  </nav>
  <div class="social" aria-label="Social links"><span></span><span></span><span></span><span></span></div>
</header>

<section class="hero abs">
  <div class="hero-photo" role="img" aria-label="Recording studio with microphone, headphones and mixing desk"></div>
  <div class="hero-card">
    <h1 class="h-title">Australia's top <span class="accent">voices professional casting</span></h1>
    <p>Tarnbelle Voices is Australia’s most successful, exclusive<br>voice over artist agency.</p>
    <span class="btn">Learn more</span>
  </div>
</section>

<section class="about">
  <div class="about-frame abs"></div>
  <div class="about-photo abs"><div role="img" aria-label="Studio microphone with pop filter against acoustic foam"></div></div>
  <h2 class="h-title abs"><span class="accent">About</span> Tarnbelle Voices</h2>
  <p class="abs">The company represents Australia’s most exceptional voices as well as high profile actors across a wide range of styles, ages, accents, characters and languages. The management team live and breathe voice overs. They are not distracted by representing anyone other than talented, professional voice artists.</p>
  <span class="btn">Learn more</span>
</section>

<section class="spotlight abs">
  <h2 class="h-title">Spotlight</h2>
  <p class="quote">Whether it be long form narration, intimate lures, snappy retail, or beyond – Corinne loves nothing more than bringing a script to life.</p>
  <p class="artist">-CORINNE ASHBY, <small>Artist - Sydney</small></p>
  <span class="btn">Play demo <span class="play"></span></span>
  <span class="sl-arrow prev"><svg width="12" height="16"><path d="M9 2 3 8l6 6" fill="none" stroke="#6aa82a" stroke-width="2.5"/></svg></span>
  <span class="sl-arrow next"><svg width="12" height="16"><path d="M3 2l6 6-6 6" fill="none" stroke="#1b3a5a" stroke-width="2.5"/></svg></span>
  <div class="spot-photo" role="img" aria-label="Voice artist standing in a home recording studio"></div>
</section>

<section class="testimonials">
  <h2 class="h-title abs">Testimonials</h2>
  <svg class="side-arrow abs" style="left:42px" width="16" height="28"><path d="M13 2 3 14l10 12" fill="none" stroke="#b5b9bd" stroke-width="2.5"/></svg>
  <div class="t-card abs" style="left:111px">
    <p>“I’ve been working with the team at Tarnbelle Voices now for almost 11 years and I’ve always found them to be very professional &amp; personable on all jobs.”</p>
    <div class="who"><span class="avatar"></span><div><div class="org">QUILLMORE</div><div class="role">Simon Rourke, National Head of Broadcast</div></div></div>
  </div>
  <div class="t-card abs" style="left:610px">
    <p>“Our business pushes the boundaries of ‘tight deadlines’ to new levels, and the team at Tarnbelle Voices save our bacon on a weekly basis.”</p>
    <div class="who"><span class="avatar"></span><div><div class="org">PENNROW</div><div class="role">Dan Mercer, Creative Director</div></div></div>
  </div>
  <svg class="side-arrow abs" style="left:1142px" width="16" height="28"><path d="M3 2l10 12L3 26" fill="none" stroke="#6aa82a" stroke-width="2.5"/></svg>
</section>

<section class="clients abs">
  <h2 class="h-title"><span class="accent">Our</span> Clients</h2>
  <svg class="side-arrow abs" style="left:42px" width="16" height="28"><path d="M13 2 3 14l10 12" fill="none" stroke="#8a9aa8" stroke-width="2.5"/></svg>
  <div class="client-row"><span>Tarrowin</span><span>Fennbrook</span><span>Oldsway</span><span>Marlowen</span><span>Ivelane</span><span>Corvale</span><span>Pennrow</span></div>
  <svg class="side-arrow abs" style="left:1142px" width="16" height="28"><path d="M3 2l10 12L3 26" fill="none" stroke="#6aa82a" stroke-width="2.5"/></svg>
</section>

<section class="news">
  <h2 class="h-title abs"><span class="accent">Latest</span> News</h2>
  <article class="n-card abs" style="left:111px">
    <div class="thumb" role="img" aria-label="Gold studio microphone in front of editing screens" style="background:linear-gradient(135deg,#5a55b8,#2b2a52 55%,#8a6a2a)"></div>
    <h3>New voice alert | Liam Hartwell</h3><span class="date">08 JAN 2021</span>
  </article>
  <article class="n-card abs" style="left:444px">
    <div class="thumb" role="img" aria-label="Producer at keyboard and monitor in a studio" style="background:linear-gradient(135deg,#a8571c,#4a2a18 50%,#2a3c5a)"></div>
    <h3>New voice alert | Owen Pritchard</h3><span class="date">10 MAY 2021</span>
  </article>
  <article class="n-card abs" style="left:775px">
    <div class="thumb" role="img" aria-label="Microphone and audio equipment in a vocal booth" style="background:linear-gradient(135deg,#6a5a48,#3a332c 55%,#8c7a62)"></div>
    <h3>New voice alert | Liam Hartwell</h3><span class="date">11 MAY 2021</span>
  </article>
</section>

<footer class="site-footer abs">
  <div class="brand"><span class="stack">TARNBELLE<small>VOICES</small></span><span class="mark"></span></div>
  <nav class="foot-nav"><span>HOME</span><span>ABOUT US</span><span>SHORTLIST</span><span>VOICES</span><span>RATES</span><span>NEWS</span><span>CONTACT US</span></nav>
  <p class="foot-line" style="top:194px"><svg width="10" height="14"><path d="M5 1a4 4 0 0 0-4 4c0 3 4 8 4 8s4-5 4-8a4 4 0 0 0-4-4z" fill="#6aa82a"/></svg>Tarnbelle Voices Pty Limited Suite 14, 88 Harbour Rd Coogee NSW 2034 Australia</p>
  <p class="foot-line" style="top:230px"><svg width="13" height="13"><path d="M3 1l3 3-2 2c1 2 2 3 4 4l2-2 3 3-2 2C6 12 1 7 1 3z" fill="#6aa82a"/></svg>SYDNEY:+ 61 2 9000 1234 &nbsp;&nbsp;| &nbsp;&nbsp;MELBOURNE:+ 61 3 9000 5678</p>
  <div class="social" aria-label="Social links"><span></span><span></span><span></span><span></span></div>
</footer>
<div class="copyright abs">2021 Company Name. All Rights Reserved</div>

</body>
</html>
```